Circular Wedding Menu Design - Adobe Illustrator

I am looking for a design for circular wedding menus. these will be 7 inches.I'm providing a template from the printer, AI files of our wedding invitation, and the menu items.

The paper our invitations were printed on was a sandy beige color. please make the background for this the same color. It will be put ontop of a white plate with ivory tablecloth and cappucino covered napkins.

IMPORTANT - We aren't committed to a specific design so feel free to use whatever you like, but we definitely want the cow, fish, and carrot images from our rsvp to be used for the entrees in the menu.

IMPORTANT - must be in Adobe illustrator format

for inspiration:
http://cdn.velvorabridalnotes.example/wp-content/uploads/2012/10/tormane-styled-19.jpg

http://www.quorbelsearch.example/imgres?imgurl=http%3A%2F%2Fwww.dellivanestudio.example%2Fblog%2Fwp-content%2Fuploads%2F2013%2F07%2FPetal-Ledger-Round-Menu-Wedding-Place-Setting.jpg&imgrefurl=http%3A%2F%2Fwww.dellivanestudio.example%2Fblog%2Finspiration%2Fsimply-lovely-wedding-menu-place-settings%2F&h=815&w=600&tbnid=8kRqzp_4LUTWEN%3A&zoom=1&docid=72HJKs9PqMxaTN&ei=QwERtYu8LpMsoBF2xdDTRk&tbm=isch&ved=0DHtRNzhKNBk&iact=rc&uact=3&dur=526&page=1&start=0&ndsp=30

https://thumbs3.pixorvane.example/images?q=tbn:QWe7KpLmNvBxRtYu2Hs4DfGhJkZxCvBnMqWeRtYuIoPaSdFgHjK

https://thumbs3.pixorvane.example/images?q=tbn:ZxC8vBnMqW_e42RT_yUioPaSdFgHjKlZxCv66BnM7q_WERtyUiOp

https://thumbs2.pixorvane.example/images?q=tbn:LkJh5GfDsAp9OiUyTrEwQ-MNbV8cXzL3KjHgFdsaPoIuYtReW0Q

Industry/Entity Type

Wedding

```html
<!DOCTYPE html>
<html lang="en">
<head>
<meta charset="utf-8">
<title>Wedding Menu</title>
<link rel="stylesheet" href="https://fonts.googleapis.com/css2?family=Pinyon+Script&family=Source+Sans+3:wght@400&display=swap">
<style>
  :root {
    --paper: #ffffff;
    --ink: #2c2618;
    --rule: #2c2618;
  }
  html, body {
    margin: 0;
    padding: 0;
    width: 1200px;
    height: 1200px;
    overflow: hidden;
    background: var(--paper);
  }
  .menu-card {
    position: relative;
    width: 1200px;
    height: 1200px;
    color: var(--ink);
    font-family: "Source Sans 3", "Myriad Pro", sans-serif;
  }
  .menu-card__frame {
    position: absolute;
    inset: 0;
  }
  .menu-card__title,
  .course-heading {
    position: absolute;
    left: 0;
    right: 0;
    margin: 0;
    text-align: center;
    font-family: "Pinyon Script", cursive;
    font-weight: 400;
    line-height: 1;
  }
  .menu-card__title {
    top: 130px;
    font-size: 178px;
  }
  .course-heading {
    font-size: 76px;
  }
  .course-heading--salad { top: 330px; }
  .course-heading--entree { top: 530px; }
  .course-heading--cake { top: 880px; }

  .course-text {
    position: absolute;
    left: 204px;
    width: 792px;
    margin: 0;
    font-size: 25.5px;
    line-height: 33px;
  }
  .course-text--salad {
    top: 423px;
    text-align: center;
  }
  .course-text--entree {
    top: 623px;
  }
  .course-text--cake {
    top: 991px;
    text-align: center;
  }
  .course-line {
    display: block;
    white-space: nowrap;
  }
  .course-line--full {
    text-align: justify;
    text-align-last: justify;
    white-space: normal;
  }
  .entree-mark {
    position: absolute;
  }
  .entree-mark--beef { left: 228px; top: 870px; width: 112px; height: 80px; }
  .entree-mark--fish { left: 876px; top: 884px; width: 116px; height: 68px; }
  .entree-mark--veggie { left: 534px; top: 1056px; width: 132px; height: 56px; }
</style>
</head>
<body>
<main class="menu-card">
  <svg class="menu-card__frame" width="1200" height="1200" viewBox="0 0 1200 1200" aria-hidden="true">
    <circle cx="600" cy="600" r="597" fill="none" stroke="var(--rule)" stroke-width="2"/>
    <circle cx="600" cy="600" r="570" fill="none" stroke="var(--rule)" stroke-width="1.6" stroke-dasharray="16 11"/>
  </svg>

  <h1 class="menu-card__title">Menu</h1>

  <h2 class="course-heading course-heading--salad">Salad:</h2>
  <p class="course-text course-text--salad">
    <span class="course-line">Grilled Watermelon &amp; Fig Salad: Gem Lettuces, Watermelon, Figs,</span>
    <span class="course-line">Toasted Hazelnuts, Balsamic Reduction, Honey-Orange Dressing</span>
  </p>

  <h2 class="course-heading course-heading--entree">Entree:</h2>
  <p class="course-text course-text--entree">
    <span class="course-line course-line--full">Beef &nbsp;- Roasted Filet Mignon, Wild Mushrooms, Garlic Mashed</span>
    <span class="course-line">Potatoes, Asparagus with Red Wine Sauce</span>
    <span class="course-line course-line--full">Fish – Porcini Crusted Halibut, Lemon-Herb Potatoes, Black Kale,</span>
    <span class="course-line">Early Girl Tomatoes</span>
    <span class="course-line course-line--full">Veggie – Artichoke Agnolotti, Wild Mushrooms, Baby Arugula,</span>
    <span class="course-line">Goat Cheese, White Wine Sauce, Micro herbs</span>
  </p>

  <svg class="entree-mark entree-mark--beef" viewBox="0 0 112 80" role="img" aria-label="Cow silhouette marking the beef entree">
    <ellipse cx="56" cy="40" rx="54" ry="36" fill="var(--ink)"/>
  </svg>
  <svg class="entree-mark entree-mark--fish" viewBox="0 0 116 68" role="img" aria-label="Fish silhouette marking the fish entree">
    <ellipse cx="58" cy="34" rx="56" ry="30" fill="var(--ink)"/>
  </svg>

  <h2 class="course-heading course-heading--cake">Wedding Cake:</h2>
  <p class="course-text course-text--cake">Delicate Butter Pecan With Fresh Raspberry Mouse.</p>

  <svg class="entree-mark entree-mark--veggie" viewBox="0 0 132 56" role="img" aria-label="Carrot silhouette marking the vegetarian entree">
    <ellipse cx="66" cy="28" rx="64" ry="22" fill="var(--ink)"/>
  </svg>
</main>
</body>
</html>
```